Pamphlet for introducing people to our church

I would like a church pamphlet designed, that includes the content in file "vosti-pamphlet.txt".

I am looking for a design that will incorporate the content in a professional and creative manner.

You do not have to use the content in any specific order, but I am relying on your skill and design knowledge to organize everything in an artistic and effective way.

Target Market(s)

Everyone

Industry/Entity Type

Religious

Requirements
Must have
• logo, use of content provided, use of branding (logo colors)
Nice to have
• More images where necessary
Should not have
• cross

```html
<!DOCTYPE html>
<html lang="en">
<head>
<meta charset="utf-8">
<title>Vosti – Church Pamphlet</title>
<link href="https://fonts.googleapis.com/css2?family=Titillium+Web:ital,wght@0,300;0,400;0,600;0,700;1,300;1,600;1,700&family=Caveat:wght@500&display=swap" rel="stylesheet">
<style>
  :root {
    --navy: #0f3a60;
    --orange: #f7941d;
    --slate: #6d6e71;
    --white: #ffffff;
    --paper: #ffffff;
  }
  * { margin: 0; padding: 0; box-sizing: border-box; }
  html, body { width: 1200px; height: 857px; overflow: hidden; background: var(--paper); }
  body { position: relative; font-family: 'Titillium Web', sans-serif; color: var(--white); }

  .page {
    position: absolute; top: 51px; width: 532px; height: 757px; overflow: hidden;
    background: var(--slate); box-shadow: 0 6px 10px rgba(0,0,0,0.18);
  }
  .page--front { left: 58px; }
  .page--back { left: 610px; }

  .divider { position: absolute; width: 2px; background: var(--orange); }
  .brand__dot { position: absolute; border-radius: 50%; background: var(--orange); }
  .brand__name { position: absolute; font-weight: 400; color: var(--white); line-height: 1; letter-spacing: 1px; white-space: nowrap; }
  .brand__tagline { position: absolute; color: var(--orange); font-weight: 400; white-space: nowrap; line-height: 1; }

  /* Front page */
  .hero {
    position: absolute; left: 0; top: 0; width: 532px; height: 603px;
    background:
      radial-gradient(ellipse 60% 35% at 45% 62%, rgba(220,235,250,0.75), rgba(220,235,250,0) 70%),
      linear-gradient(180deg, #0f3a60 0%, #1c4f7c 35%, #4f7ca6 55%, #8a8e9a 70%, #d99a4a 82%, #1a1410 90%, #0a0806 100%);
  }
  .service {
    position: absolute; left: 0; top: 30px; width: 220px; text-align: right;
    color: var(--orange); font-weight: 700; font-size: 17.5px; line-height: 22px;
  }
  .contact {
    position: absolute; left: 0; top: 93px; width: 220px; text-align: right;
    font-size: 14.4px; line-height: 18.4px;
  }
  .front .brand__dot { left: 272px; top: 100px; width: 18px; height: 18px; }
  .front .brand__name { left: 298px; top: 69px; font-size: 70px; }
  .front .brand__tagline { left: 291px; top: 135px; font-size: 11px; letter-spacing: 1px; }

  .mission {
    position: absolute; left: 140px; top: 210px; width: 254px; text-align: center;
    color: var(--orange); font-style: italic; font-weight: 700; font-size: 17px; line-height: 21.3px;
  }
  .intro {
    position: absolute; top: 633px; font-style: italic; font-weight: 300; font-size: 14.4px; line-height: 18.4px;
  }
  .intro--left { left: 40px; width: 184px; text-align: right; }
  .intro--right { left: 272px; width: 240px; }

  /* Back page */
  .candle-photo {
    position: absolute; left: 182px; top: -15px; width: 408px; height: 408px; border-radius: 50%;
    background:
      radial-gradient(circle at 60% 64%, rgba(255,235,180,0.95) 0 4%, rgba(245,190,110,0.7) 10%, rgba(190,95,40,0.55) 22%, rgba(90,35,15,0.3) 34%, rgba(0,0,0,0) 46%),
      #0b0806;
  }
  .scripture {
    position: absolute; left: 226px; top: 26px; width: 280px; text-align: right;
    font-family: 'Caveat', cursive; font-weight: 500; color: var(--orange); font-size: 17px; line-height: 17px;
  }
  .belief {
    position: absolute; left: 42px; top: 83px; width: 160px;
    font-style: italic; font-weight: 300; font-size: 14.4px; line-height: 18.4px;
  }
  .belief p + p { margin-top: 18.4px; }

  .ministries { position: absolute; left: 42px; top: 402px; width: 480px; }
  .ministry { padding-left: 7px; border-left: 2px solid var(--orange); margin-bottom: 18.4px; }
  .ministry__heading { color: var(--orange); font-weight: 700; font-size: 14.5px; line-height: 18.4px; }
  .ministry__name { color: var(--orange); font-style: italic; font-weight: 700; font-size: 14.4px; line-height: 18.4px; }
  .ministry__desc { font-style: italic; font-weight: 300; font-size: 14.4px; line-height: 18.4px; }

  .footer-band { position: absolute; left: 0; top: 602px; width: 532px; height: 155px; background: var(--navy); }
  .address {
    position: absolute; left: 0; top: 25px; width: 272px; text-align: right;
    font-size: 14px; line-height: 19.2px;
  }
  .footer-band .brand__dot { left: 308px; top: 58px; width: 11px; height: 11px; }
  .footer-band .brand__name { left: 324px; top: 44px; font-size: 40px; }
  .footer-band .brand__tagline { left: 322px; top: 79px; font-size: 7.5px; letter-spacing: 0.6px; }
  .reach {
    position: absolute; left: 0; top: 104px; width: 532px; text-align: center;
    font-size: 13.5px; line-height: 17px;
  }
  .reach strong { color: var(--orange); font-weight: 600; }
</style>
</head>
<body>

<section class="page page--front front">
  <div class="hero" role="img" aria-label="Photo: silhouette of a person with raised arms against a sunset sky with light rays"></div>

  <div class="service">SUNDAY SERVICE:<br>10:00am - 12:30pm</div>
  <div class="contact">www.vosti.org<br>contact@cedarhillfold.org<br>+1 555-014-2280</div>
  <div class="divider" style="left:249px; top:33px; height:112px;"></div>

  <span class="brand__dot"></span>
  <span class="brand__name">VOSTI</span>
  <span class="brand__tagline">A LIGHT FOR EVERY PEOPLE</span>

  <p class="mission">VOSTI is a gathering of believers whose purpose is to seek the face of God for an authentic restoration of the church as a body of born again believers around the world.</p>

  <p class="intro intro--left">As a gathering of believers,<br>VOSTI seeks an awakening of<br>the mind founded on the<br>precepts and teachings of<br>Jesus Christ.</p>
  <div class="divider" style="left:249px; top:629px; height:108px;"></div>
  <p class="intro intro--right">The modern church has replaced the<br>simple and Kingdom centered<br>principles of Jesus’s disciples with<br>complacent and compromised<br>teachings on earthly prosperity.</p>
</section>

<section class="page page--back">
  <div class="candle-photo" role="img" aria-label="Photo: cupped hands holding a lit candle in the dark"></div>
  <p class="scripture">“If my people, which are called by my name,<br>shall humble themselves, and pray, and seek my<br>face, and turn from their wicked ways; then will I<br>hear from heaven, and will forgive their sin, and<br>will heal their land.” 2 Chronicles 7:14</p>

  <div class="belief">
    <p>We believe in<br>humbly seeking<br>God without<br>motive to use<br>God or His Word<br>for our own gain.</p>
    <p>The end times<br>church will<br>experience a<br>glorious revival,<br>renewed love and zeal<br>for true discipleship,<br>faith, and godliness as<br>Jesus intended for us.</p>
  </div>

  <div class="ministries">
    <div class="ministry">
      <div class="ministry__heading">MINISTRIES:</div>
      <div class="ministry__name">Kingdom seeds (Children’s ministry)</div>
      <div class="ministry__desc">Children learn to be seeds of godliness in the world.</div>
    </div>
    <div class="ministry">
      <div class="ministry__name">School of pilgrims</div>
      <div class="ministry__desc">Learn the basics of Christian faith and about God’s purpose for your life.</div>
    </div>
    <div class="ministry">
      <div class="ministry__name">School of disciples</div>
      <div class="ministry__desc">Deepen your knowledge of God’s word and learn how to server him.</div>
    </div>
  </div>

  <div class="footer-band">
    <div class="address">Alder Community Hall<br>48 Linden Avenue,<br>Fairhaven, ME 04999</div>
    <div class="divider" style="left:292px; top:23px; height:60px;"></div>
    <span class="brand__dot"></span>
    <span class="brand__name">VOSTI</span>
    <span class="brand__tagline">A LIGHT FOR EVERY PEOPLE</span>
    <p class="reach"><strong>If you need prayer or counseling give us a call at</strong> +1 555-014-2280<br><strong>or email us at</strong> contact@cedarhillfold.org</p>
  </div>
</section>

</body>
</html>
```